Product Designer Business Card

Small product design, engineering and prototyping firm in need of a clean, professional business card design. To support our 3D design and drawing services, we offer 3D printing, molding, and casting of plastics, silicones, resins, etc. Our logo can still be modified/changed if necessary. The red/orange color is preferred, but may be substituted with blue or green, potentially. Either way, the colour of the logo should be match/compliment colors used throughout the design. One thought is to have the logo/contact info on one side, with the other side describing services offered, like with a small icon of 3D printer, molding, casting, and computer with a 3D model on-screen.
Industry/Entity Type
Mechanical Engineering
Contact Information for Business Card
Company: Velkin Design
Phone: 613-555-0147
Email: marc@velkindesign.ca

```html
<!DOCTYPE html>
<html lang="en">
<head>
<meta charset="utf-8">
<title>Velkin Design – Business Card</title>
<link href="https://fonts.googleapis.com/css2?family=Open+Sans:wght@400;600&display=swap" rel="stylesheet">
<style>
  :root {
    --backdrop: #3b3b3d;
    --card: #1c1c1d;
    --red: #e0232b;
    --white: #f4f4f4;
    --icon-fill-a: #2c2c2e;
    --icon-fill-b: #3a3a3c;
  }
  * { margin: 0; padding: 0; box-sizing: border-box; }
  html, body {
    width: 1200px; height: 1021px; overflow: hidden;
    background: var(--backdrop);
    font-family: "Open Sans", sans-serif;
  }
  .card {
    position: absolute; left: 220px;
    width: 760px; height: 434px;
    background: var(--card);
    box-shadow: 0 14px 30px rgba(0,0,0,.45);
  }
  .card--services { top: 52px; }
  .card--contact { top: 535px; }

  .brand { display: flex; align-items: center; gap: 16px; }
  .brand__dot { width: 46px; height: 46px; border-radius: 50%; background: var(--red); }
  .brand__name { font-size: 44px; font-weight: 600; color: var(--red); letter-spacing: 1px; }

  .card--services .brand { position: absolute; top: 62px; left: 0; right: 0; justify-content: center; }
  .services {
    position: absolute; top: 190px; left: 60px; right: 60px;
    display: flex; justify-content: space-between; list-style: none;
  }
  .service { width: 140px; display: flex; flex-direction: column; align-items: center; gap: 14px; }
  .service__icon {
    width: 100px; height: 100px; border-radius: 6px;
    background: linear-gradient(145deg, var(--icon-fill-b), var(--icon-fill-a));
    border: 1px solid #4a4a4c;
  }
  .service__label { color: var(--red); font-size: 19px; }

  .card--contact .brand { position: absolute; top: 170px; left: 60px; }
  .contact { position: absolute; top: 150px; left: 440px; color: var(--white); }
  .contact__name { color: var(--red); font-size: 25px; font-weight: 600; }
  .contact__role { font-size: 19px; margin-bottom: 18px; }
  .contact__list { list-style: none; font-size: 19px; line-height: 30px; }
  .contact__list li { display: flex; align-items: center; gap: 10px; }
  .contact__list svg { width: 17px; height: 17px; flex: none; }
</style>
</head>
<body>
  <section class="card card--services">
    <div class="brand">
      <span class="brand__dot"></span>
      <span class="brand__name">Velkin Design</span>
    </div>
    <ul class="services">
      <li class="service"><div class="service__icon" role="img" aria-label="Line icon of a 3D printer"></div><span class="service__label">3D Printing</span></li>
      <li class="service"><div class="service__icon" role="img" aria-label="Line icon of a molding machine"></div><span class="service__label">Molding</span></li>
      <li class="service"><div class="service__icon" role="img" aria-label="Line icon of resin being poured into a casting mold"></div><span class="service__label">Casting</span></li>
      <li class="service"><div class="service__icon" role="img" aria-label="Line icon of a computer showing a 3D model"></div><span class="service__label">3d Model</span></li>
    </ul>
  </section>

  <section class="card card--contact">
    <div class="brand">
      <span class="brand__dot"></span>
      <span class="brand__name">Velkin Design</span>
    </div>
    <div class="contact">
      <p class="contact__name">Marc Halden</p>
      <p class="contact__role">Owner</p>
      <ul class="contact__list">
        <li>
          <svg viewBox="0 0 24 24" aria-hidden="true"><path fill="#e0232b" d="M6.6 10.8a15 15 0 0 0 6.6 6.6l2.2-2.2a1 1 0 0 1 1-.25 11.4 11.4 0 0 0 3.6.57 1 1 0 0 1 1 1V20a1 1 0 0 1-1 1A17 17 0 0 1 3 4a1 1 0 0 1 1-1h3.5a1 1 0 0 1 1 1c0 1.25.2 2.45.57 3.6a1 1 0 0 1-.25 1z"/></svg>
          <span>613-555-0147</span>
        </li>
        <li>
          <svg viewBox="0 0 24 24" aria-hidden="true"><rect x="2.5" y="5" width="19" height="14" fill="none" stroke="#e0232b" stroke-width="2"/><path d="M3 6l9 7 9-7" fill="none" stroke="#e0232b" stroke-width="2"/></svg>
          <span>marc@velkindesign.ca</span>
        </li>
        <li>
          <svg viewBox="0 0 24 24" aria-hidden="true"><g fill="none" stroke="#e0232b" stroke-width="1.8"><circle cx="12" cy="12" r="9.5"/><ellipse cx="12" cy="12" rx="4" ry="9.5"/><path d="M2.5 12h19M4 7h16M4 17h16"/></g></svg>
          <span>www.velkindesign.ca</span>
        </li>
      </ul>
    </div>
  </section>
</body>
</html>
```